Colin + Rob's 30th Birthday FB event cover photo

We're after a Facebook even cover photo for our 30th B'day. We live in Sydney
Colin + Rob's 30th Birthday

Venue (these details can be used in the graphic):
Quiet Heron
the basement of
The Marlow Hotel
58 Brindle St Hollerby
2 August 8pm-3am

The Marlow logo: http://www.themarlowhotelvenue.com
Quiet Heron logo: http://quietheronhoot.com.au
The horizontal FaceBook cover photo for events has specific dimensions
As ideas I kind of like the styling of the dj poster (file attached) as a rough guide but not essential (i.e. no need to stick to that format/colours/dark shades) and Also the poster Pixel Fold's Renzo did for Mirth Up
Thanks!

```html
<!DOCTYPE html>
<html lang="en">
<head>
<meta charset="utf-8">
<title>Colin + Rob's 30th Birthday</title>
<link rel="stylesheet" href="https://fonts.googleapis.com/css2?family=Fredoka:wght@600&family=Josefin+Sans:wght@300&display=swap">
<style>
  :root {
    --bg-deep: #2a120c;
    --bg-dark: #4a1f14;
    --bg-mid: #7a3422;
    --bg-warm: #b25538;
    --bg-glow: #d98660;
    --text-peach: #f7d2b8;
    --border-tone: rgba(247, 210, 184, 0.7);
    --text-faded: rgba(247, 210, 184, 0.5);
    --venue-red: #d8431f;
  }
  * { margin: 0; padding: 0; box-sizing: border-box; }
  html, body { width: 1200px; height: 443px; overflow: hidden; background: var(--bg-deep); }
  .cover {
    position: relative;
    width: 1200px;
    height: 443px;
    overflow: hidden;
    font-family: "Fredoka", "Arial Rounded MT Bold", sans-serif;
    font-weight: 600;
    color: var(--text-peach);
  }
  .cover__backdrop {
    position: absolute;
    inset: 0;
    background:
      linear-gradient(180deg, transparent 22%, rgba(42, 18, 12, 0.45) 30%, rgba(42, 18, 12, 0.45) 64%, transparent 72%),
      radial-gradient(ellipse 45% 65% at 50% 45%, rgba(217, 134, 96, 0.55), transparent 70%),
      radial-gradient(ellipse 35% 70% at 95% 35%, rgba(178, 85, 56, 0.75), transparent 75%),
      radial-gradient(ellipse 35% 70% at 3% 30%, rgba(74, 31, 20, 0.85), transparent 75%),
      linear-gradient(180deg, var(--bg-dark) 0%, var(--bg-mid) 35%, var(--bg-warm) 60%, var(--bg-mid) 85%, var(--bg-dark) 100%);
  }
  .cover__date {
    position: absolute;
    top: 26px;
    left: 0;
    width: 100%;
    text-align: center;
    font-size: 34px;
    letter-spacing: 2px;
    text-transform: uppercase;
  }
  .cover__border {
    position: absolute;
    left: 194px;
    width: 812px;
    height: 10px;
    background: var(--border-tone);
  }
  .cover__border--top { top: 90px; }
  .cover__border--bottom { top: 293px; }
  .cover__title {
    position: absolute;
    top: 106px;
    left: 0;
    width: 100%;
    text-align: center;
    font-size: 100px;
    font-weight: 600;
    line-height: 88px;
    letter-spacing: 6px;
    text-transform: uppercase;
  }
  .cover__venue-name {
    position: absolute;
    top: 362px;
    left: 0;
    width: 100%;
    text-align: center;
    font-size: 30px;
    letter-spacing: 4px;
    color: var(--venue-red);
    text-transform: uppercase;
  }
  .cover__address {
    position: absolute;
    top: 405px;
    left: 192px;
    width: 822px;
    display: flex;
    justify-content: space-between;
    font-family: "Josefin Sans", "Helvetica Neue", sans-serif;
    font-weight: 300;
    font-size: 23px;
    letter-spacing: 0.5px;
    color: var(--text-faded);
    text-transform: uppercase;
  }
</style>
</head>
<body>
  <main class="cover">
    <div class="cover__backdrop" role="img" aria-label="Background texture of overlapping translucent angular shards in rust and amber tones"></div>

    <p class="cover__date">2 August 8pm - 3am</p>

    <div class="cover__border cover__border--top" role="img" aria-label="Zigzag border ornament above the title"></div>

    <h1 class="cover__title">Colin + Rob's<br>30th Birthday</h1>

    <div class="cover__border cover__border--bottom" role="img" aria-label="Zigzag border ornament below the title"></div>

    <p class="cover__venue-name">Quiet Heron</p>

    <p class="cover__address">
      <span class="cover__street">58 Brindle St Hollerby</span>
      <span class="cover__location">The basement of the Marlow Hotel</span>
    </p>
  </main>
</body>
</html>
```